Consulting group
Business cards and stationary
Use same font as used in my logo
I think it is Swiss721?
Simple
Damon Fairley
President
417 W. Marlow Avenue, Apt 118 Ann Arbor, MI 48177
Damon@DamonFairley.com
www.TheCopperLantern.com
Looking for envelope, letterhead, and business card.
the logo? if you want to try putting a quote on it: "“The worst thing that can happen to a good cause is, not to be skillfully attacked, but to be ineptly defended.” - Corvelle. Not sure if I will like the quote on there or not.

```html
<!DOCTYPE html>
<html lang="en">
<head>
<meta charset="utf-8">
<title>The Copper Lantern — Stationery</title>
<link rel="stylesheet" href="https://fonts.googleapis.com/css2?family=Archivo:wght@400;700;800&display=swap">
<style>
  :root {
    --brand-red: #e3222b;
    --ink: #1a1a1a;
    --paper: #ffffff;
    --backdrop: #8a8a8a;
    --fold-line: #d6d6d6;
    --muted: #555555;
  }
  * { box-sizing: border-box; margin: 0; padding: 0; }
  html, body { width: 1200px; height: 775px; overflow: hidden; }
  body {
    background: var(--backdrop);
    font-family: "Archivo", "Helvetica Neue", Arial, sans-serif;
    color: var(--ink);
    position: relative;
  }
  .sheet {
    position: absolute;
    background: var(--paper);
    box-shadow: 0 6px 18px rgba(0,0,0,.25);
    overflow: hidden;
  }

  /* wordmark */
  .wordmark { display: flex; align-items: center; gap: 8px; }
  .wordmark-square { background: var(--brand-red); flex: none; }
  .wordmark-name {
    font-weight: 800; color: var(--ink); line-height: .95;
    letter-spacing: -.01em;
  }

  /* letterhead */
  .letterhead { left: 60px; top: 40px; width: 500px; height: 680px; }
  .letterhead-band {
    position: absolute; left: 0; top: 34px; width: 340px; height: 42px;
    background: var(--brand-red); color: var(--paper);
    display: grid; grid-template-columns: 1fr 1fr; align-content: center;
    padding: 0 18px; column-gap: 14px; font-size: 8px; line-height: 1.4;
  }
  .letterhead-rule {
    position: absolute; left: 0; right: 0; top: 80px; height: 2px;
    background: var(--brand-red);
  }
  .letterhead .wordmark { position: absolute; right: 26px; top: 26px; }
  .letterhead .wordmark-square { width: 44px; height: 44px; }
  .letterhead .wordmark-name { font-size: 17px; }

  /* envelope back */
  .envelope-back { left: 640px; top: 40px; width: 500px; height: 230px; }
  .envelope-flap { position: absolute; inset: 0; }
  .envelope-back .wordmark-square {
    position: absolute; left: 238px; top: 78px; width: 24px; height: 24px;
  }

  /* envelope front */
  .envelope-front { left: 640px; top: 300px; width: 500px; height: 230px; }
  .envelope-band {
    position: absolute; left: 0; right: 0; top: 34px; height: 26px;
    background: var(--brand-red);
  }
  .envelope-front .wordmark { position: absolute; right: 22px; top: 74px; }
  .envelope-front .wordmark-square { width: 40px; height: 40px; }
  .envelope-front .wordmark-name { font-size: 15px; }
  .envelope-web {
    position: absolute; right: 22px; top: 124px;
    font-size: 8px; color: var(--muted);
  }

  /* business cards */
  .card { width: 330px; height: 190px; border-radius: 10px; }
  .card-front { left: 640px; top: 560px; width: 250px; height: 160px; }
  .card-back { left: 910px; top: 560px; width: 230px; height: 160px; }

  .card-name {
    position: absolute; left: 16px; top: 16px;
    font-size: 12px; font-weight: 700; color: var(--brand-red);
  }
  .card-title {
    position: absolute; left: 16px; top: 31px;
    font-size: 8px; color: var(--muted);
  }
  .card-details {
    position: absolute; left: 16px; top: 50px;
    font-size: 7px; line-height: 1.5; color: var(--ink); list-style: none;
  }
  .card-band {
    position: absolute; left: 0; right: 0; bottom: 14px; height: 20px;
    background: var(--brand-red); color: var(--paper);
    font-size: 8px; font-weight: 700; padding-left: 16px;
    display: flex; align-items: center;
  }
  .card-front .wordmark { position: absolute; right: 14px; bottom: 40px; }
  .card-front .wordmark-square { width: 34px; height: 34px; }
  .card-front .wordmark-name { font-size: 12px; }

  .card-back .wordmark-square {
    position: absolute; left: 22px; top: 46px; width: 26px; height: 26px;
  }
  .card-back-web {
    position: absolute; left: 22px; top: 84px;
    font-size: 8px; color: var(--brand-red);
  }
</style>
</head>
<body>

  <section class="sheet letterhead" aria-label="Letterhead">
    <div class="letterhead-band">
      <span>417 W. Marlow Avenue, Apt 118<br>Ann Arbor, MI 48177</span>
      <span>(734) 555-0142<br>Damon@DamonFairley.com</span>
    </div>
    <div class="letterhead-rule"></div>
    <div class="wordmark">
      <span class="wordmark-square"></span>
      <span class="wordmark-name">The<br>Copper<br>Lantern</span>
    </div>
  </section>

  <section class="sheet envelope-back" aria-label="Envelope back">
    <svg class="envelope-flap" viewBox="0 0 500 230" aria-hidden="true">
      <polyline points="0,0 250,130 500,0" fill="none" stroke="var(--fold-line)" stroke-width="1.5"/>
      <polyline points="0,230 200,110" fill="none" stroke="var(--fold-line)" stroke-width="1"/>
      <polyline points="500,230 300,110" fill="none" stroke="var(--fold-line)" stroke-width="1"/>
    </svg>
    <span class="wordmark-square"></span>
  </section>

  <section class="sheet envelope-front" aria-label="Envelope front">
    <div class="envelope-band"></div>
    <div class="wordmark">
      <span class="wordmark-square"></span>
      <span class="wordmark-name">The<br>Copper<br>Lantern</span>
    </div>
    <p class="envelope-web">417 W. Marlow Avenue, Apt 118 Ann Arbor, MI 48177</p>
  </section>

  <section class="sheet card card-front" aria-label="Business card front">
    <h1 class="card-name">Damon Fairley</h1>
    <p class="card-title">President</p>
    <ul class="card-details">
      <li>417 W. Marlow Avenue, Apt 118</li>
      <li>Ann Arbor, MI 48177</li>
      <li>(734) 555-0142</li>
      <li>Damon@DamonFairley.com</li>
    </ul>
    <div class="wordmark">
      <span class="wordmark-square"></span>
      <span class="wordmark-name">The<br>Copper<br>Lantern</span>
    </div>
    <div class="card-band">www.TheCopperLantern.com</div>
  </section>

  <section class="sheet card card-back" aria-label="Business card back">
    <span class="wordmark-square"></span>
    <p class="card-back-web">www.TheCopperLantern.com</p>
  </section>

</body>
</html>
```